Verdant Loop Advisors, LLC

I am looking for a simple, clear layout with my logo prominent and embossed, on the best quality card stock available. I would like the business name and phone number included on the card as well......I dont want my name anywhere on the card and I would like my logo embossed on the card......something simple with a white back......open to designs as long as they go along with recycling symbols and green type stuff.....The address, website, cell number, fax number, and email are listed below

5374 Tillbury Fenwood Road
Larkfield, MD 20799

c. 240.555.0143 f. 240.555.0187
e. sales@verdantloopadvisors.example
w. www.verdantloopadvisors.example

Industry/Entity Type

Recycling

```html
<!DOCTYPE html>
<html lang="en">
<head>
<meta charset="utf-8">
<title>Verdant Loop Advisors, LLC – Business Card</title>
<link rel="stylesheet" href="https://fonts.googleapis.com/css2?family=Source+Sans+3:wght@400;700&display=swap">
<style>
  :root {
    --page-bg: #ffffff;
    --card-bg: #ffffff;
    --card-border: #1a1a1a;
    --ink: #111111;
    --brand-ink: #1f1d12;
    --leaf-green: #2a7a32;
  }
  html, body {
    margin: 0;
    padding: 0;
    width: 1200px;
    height: 927px;
    overflow: hidden;
    background: var(--page-bg);
  }
  .canvas {
    position: relative;
    width: 1200px;
    height: 927px;
    font-family: "Source Sans 3", "Myriad Pro", Arial, sans-serif;
    color: var(--ink);
  }
  .business-card {
    position: absolute;
    left: 190px;
    top: 265px;
    width: 784px;
    height: 370px;
    background: var(--card-bg);
    border: 2px solid var(--card-border);
  }
  .brand-mark {
    position: absolute;
    left: 48px;
    top: 52px;
    width: 150px;
    height: 150px;
  }
  .brand-name {
    position: absolute;
    right: 96px;
    top: 58px;
    margin: 0;
    font-size: 37px;
    font-weight: 700;
    line-height: 1;
    color: var(--brand-ink);
    white-space: nowrap;
  }
  .contact-block {
    position: absolute;
    left: 441px;
    top: 202px;
    margin: 0;
    font-style: normal;
    font-size: 21px;
    line-height: 27px;
    white-space: nowrap;
  }
  .contact-block span { display: block; }
  .phone-line {
    position: absolute;
    left: 34px;
    top: 313px;
    margin: 0;
    font-size: 21px;
    line-height: 27px;
    white-space: nowrap;
  }
</style>
</head>
<body>
  <main class="canvas">
    <section class="business-card">
      <svg class="brand-mark" viewBox="0 0 150 150" aria-hidden="true">
        <circle cx="75" cy="75" r="70" fill="var(--leaf-green)"/>
      </svg>
      <h1 class="brand-name">Verdant Loop Advisors, LLC</h1>

      <address class="contact-block">
        <span>5374 Tillbury Fenwood Road</span>
        <span>Larkfield, MD 20799</span>
        <span>www.verdantloopadvisors.example</span>
        <span>sales@verdantloopadvisors.example</span>
        <span>Fax 240 555 0187</span>
      </address>

      <p class="phone-line">Tel&nbsp; 240 555 0143</p>
    </section>
  </main>
</body>
</html>
```